Hello,
Corinne Haskett Equestrian needs a business card. We are a high performance show jumping stables based at Willowmere Reserve in morningotn. We pride ourselves on producing high quality show jumping horses and competing our stock at a high level. My business card need to have my logo on it, and i would like it to have a classic design with a modern touch. I would like it to have quite a natural feel about it. It needs to be in a font which is easy to read as I spend a lot of time competing internationally and overseas, and i need to be able to give it out to breeders and contacts where English isnt their first language. I will need it to include the following details:
-Corinne Haskett Equestrian
-Based at Willowmere Reserve Mornington
-Address: 17 Tremont Lane Mornington Victoria 3931
-Mobile number: 0412605948
- website: www.corinnehaskettequestrian.example
Target Market(s)
For business adults who english may not be their first language
Industry/Entity Type
Business

```html
<!DOCTYPE html>
<html lang="en">
<head>
<meta charset="utf-8">
<title>Corinne Haskett Equestrian – Business Card</title>
<link rel="stylesheet" href="https://fonts.googleapis.com/css2?family=Cinzel:wght@400;500&display=swap">
<style>
  :root {
    --paper: #ffffff;
    --amber-light: #dc8834;
    --amber-mid: #cf7a30;
    --amber-deep: #b25f27;
    --brand: #a85622;
    --ink: #0d0d0d;
    --text-light: #ffffff;
  }
  html, body {
    margin: 0;
    padding: 0;
    width: 1200px;
    height: 720px;
    overflow: hidden;
    background: var(--paper);
  }
  .card {
    position: relative;
    width: 1200px;
    height: 720px;
    overflow: hidden;
    background: var(--paper);
    font-family: "Cinzel", "Times New Roman", serif;
  }
  .card__sweep {
    position: absolute;
    inset: 0;
    width: 1200px;
    height: 720px;
  }
  .brand {
    position: absolute;
    top: 60px;
    right: 44px;
    margin: 0;
    text-align: right;
  }
  .brand__name {
    margin: 0;
    font-family: "Cinzel", "Times New Roman", serif;
    font-weight: 500;
    font-size: 46px;
    line-height: 1.15;
    letter-spacing: 2px;
    color: var(--brand);
  }
  .brand__base {
    margin: 14px 0 0;
    font-family: "Cinzel", "Times New Roman", serif;
    font-weight: 400;
    font-size: 18px;
    letter-spacing: 1px;
    color: var(--ink);
    white-space: nowrap;
  }
  .contact-list {
    position: absolute;
    left: 126px;
    top: 436px;
    margin: 0;
    padding: 0;
    list-style: none;
  }
  .contact-list__item {
    display: flex;
    align-items: center;
    height: 60px;
    margin-bottom: 24px;
    color: var(--text-light);
    font-size: 29px;
    font-weight: 400;
    letter-spacing: 0.5px;
    white-space: nowrap;
  }
  .contact-list__item:last-child { margin-bottom: 0; }
  .contact-list__icon {
    width: 60px;
    height: 52px;
    flex: none;
    margin-right: 26px;
  }
</style>
</head>
<body>
  <main class="card">
    <svg class="card__sweep" viewBox="0 0 1200 720" aria-hidden="true">
      <defs>
        <radialGradient id="amberGlow" cx="330" cy="340" r="760" gradientUnits="userSpaceOnUse">
          <stop offset="0" stop-color="#dc8834"/>
          <stop offset="0.45" stop-color="#cf7a30"/>
          <stop offset="1" stop-color="#b25f27"/>
        </radialGradient>
      </defs>
      <path d="M0 0 Q 800 250 1200 720 L 0 720 Z" fill="url(#amberGlow)"/>
    </svg>

    <header class="brand">
      <h1 class="brand__name">Corinne Haskett<br>Equestrian</h1>
      <p class="brand__base">Based at Willowmere Reserve Mornington</p>
    </header>

    <ul class="contact-list">
      <li class="contact-list__item">
        <svg class="contact-list__icon" viewBox="0 0 60 52" aria-hidden="true">
          <polygon points="15,0 45,0 60,26 45,52 15,52 0,26" fill="#0d0d0d"/>
          <g fill="none" stroke="#ffffff" stroke-width="2.2">
            <circle cx="30" cy="26" r="14"/>
            <ellipse cx="30" cy="26" rx="6.5" ry="14"/>
            <line x1="16" y1="26" x2="44" y2="26"/>
            <line x1="30" y1="12" x2="30" y2="40"/>
            <path d="M18 18 H42 M18 34 H42"/>
          </g>
        </svg>
        <span class="contact-list__text">www.corinnehaskettequestrian.example</span>
      </li>
      <li class="contact-list__item">
        <svg class="contact-list__icon" viewBox="0 0 60 52" aria-hidden="true">
          <polygon points="15,0 45,0 60,26 45,52 15,52 0,26" fill="#0d0d0d"/>
          <rect x="20" y="9" width="20" height="34" rx="3" fill="#ffffff"/>
          <rect x="23" y="13" width="14" height="24" fill="#0d0d0d"/>
          <circle cx="30" cy="40" r="1.4" fill="#0d0d0d"/>
        </svg>
        <span class="contact-list__text">0412605948</span>
      </li>
      <li class="contact-list__item">
        <svg class="contact-list__icon" viewBox="0 0 60 52" aria-hidden="true">
          <polygon points="15,0 45,0 60,26 45,52 15,52 0,26" fill="#0d0d0d"/>
          <path d="M30 10 L46 25 L42 25 L42 40 L34 40 L34 31 L26 31 L26 40 L18 40 L18 25 L14 25 Z" fill="#ffffff"/>
        </svg>
        <span class="contact-list__text">Address: 17 Tremont Lane Mornington Victoria 3931</span>
      </li>
    </ul>
  </main>
</body>
</html>
```